Horizontal scrolling homepage | ||
Consulting company needing a unique layout | ||
Consulting | ||
Qorvinex does consulting and implementation projects within CRM which are the processes around sales, marketing, service, call centers, web shops and more. Even though such engagements of course need the technical involvement from IT, it for sure also needs the business and in this segment the business consists of extrovert colorful people. |
The homepage must be different than the competitors and one way of doing that is by having horizontal scrolling with a menu bar on the left (if the design would be better, you can place it on the top). If it can be done in a cool way, then the left menu bar could be a bit to the right of the left border so that the scrolling background is visible. The scrolling should accelerate and de-accelerate when moving to the part of the homepage that should be displayed. There should not be a scrollbar. Menu: Start (or logo) Packages Services Next Step Career About On the start page there should be a combined sign up for newsletter and contact form (like here: brimtala[dot]dk[slash]om-brimtala). (Title, first name, last name, e-mail, mobile phone number, checkbox for Newsletter sign up and a free text field). The homepage must be easy to extend with additional texts. There should be teasers on the start page that will navigate the user to a place on one of the subpages with more information. It could be interesting to have flipping boxes like in Window Mobile, where one side of the box has a teaser one-liner and when the mouse hovers over it flips and the solution is on the back and when clicked, the page scrolls to the place with more information. But I do not know how easy that will be to implement with HTML5. Inspire me. In addition add the content that normally is part of a start page. You will find logo and teasers as attachments. For additional text use dummy latin. |
Cutting-Edge Unique/Creative Flashy Professional Corporate Modern Elegant Service Oriented |
See logo | ||
Arial Verdana Trebuchet MS |
left side | ||
http://www.morvenquaily.co.uk/ | ||
http://www.pravessa.com/ | ||
http://tunbelfield.com/ | ||
The homepage should be compatible with Internet Explorer and Crome, it should be accessible from Android pads and phones and Apple Iphones and Ipads, but I assume that will all automatically be possible when HTML5 is used for the development. The homepage must be easy to extend with additional menu items / texts. |

```html
<!DOCTYPE html>
<html lang="en">
<head>
<meta charset="utf-8">
<title>Qorvinex</title>
<link rel="stylesheet" href="https://fonts.googleapis.com/css2?family=PT+Sans:ital,wght@0,400;0,700;1,400&display=swap">
<style>
:root{
  --green:#7cc242;
  --green-dark:#5fa52c;
  --navy:#2d4a6b;
  --blue:#1e6fb8;
  --blue-sky:#2a8fd6;
  --blue-deep:#0f5fa8;
  --title:#1f7cc4;
  --text-grey:#8a8a8a;
  --white:#ffffff;
  --ink:#333a44;
}
*{box-sizing:border-box;margin:0;padding:0}
html,body{width:1200px;height:590px;overflow:hidden}
body{font-family:"PT Sans",sans-serif;background:var(--blue-deep);position:relative}
.backdrop{position:absolute;left:0;top:0;width:1200px;height:590px;
  background:radial-gradient(ellipse at 60% 40%,var(--blue-sky) 0%,var(--blue) 45%,var(--blue-deep) 100%)}
.social-rail{position:absolute;left:0;top:0;width:24px;height:590px;background:var(--green);z-index:2}
.social-rail .dot{position:absolute;left:4px;width:16px;height:16px;border-radius:50%;background:var(--white)}
.social-rail .label{position:absolute;left:2px;bottom:12px;writing-mode:vertical-rl;transform:rotate(180deg);
  color:var(--white);font-size:11px;font-weight:700;letter-spacing:.3px}
.sidebar{position:absolute;left:24px;top:0;width:259px;height:590px;background:var(--white)}
.brand{position:absolute;left:44px;top:28px;display:flex;align-items:center;gap:10px}
.brand .mark{width:30px;height:30px;border-radius:50%;background:var(--green)}
.brand .name{font-size:30px;font-weight:700;color:var(--navy);line-height:1}
.menu{position:absolute;top:98px;left:0;list-style:none}
.menu li{position:absolute;height:28px;line-height:28px;color:var(--white);font-size:13px;font-weight:700;
  text-align:center;text-transform:uppercase;background:var(--green);width:160px;left:86px;white-space:nowrap}
.menu li.active{background:var(--navy);left:72px;width:174px;height:32px;line-height:32px}
.footer-note{position:absolute;left:40px;top:538px;width:210px;font-size:9px;line-height:12px;color:var(--ink)}
.footer-note b{font-weight:700}
.teaser{position:absolute;top:94px;width:216px;height:284px;background:var(--white);border-radius:8px;overflow:hidden;
  box-shadow:0 2px 6px rgba(0,0,0,.25)}
.teaser .photo{height:122px;margin:8px 8px 0;border-radius:4px}
.teaser h3{margin:8px 10px 0;font-size:14px;line-height:16px;color:var(--title);font-weight:700}
.teaser p{margin:6px 10px 0;font-size:10px;line-height:13px;color:var(--text-grey);font-style:italic}
.teaser .details{position:absolute;bottom:10px;right:10px;width:58px;height:20px;border-radius:4px;background:var(--green);
  color:var(--white);font-size:11px;text-align:center;line-height:20px}
.teaser.first .details{right:auto;left:80px}
.photo.laptop{background:linear-gradient(135deg,#d9e3ea,#a9b8c4 60%,#7f8e9a)}
.photo.team{background:linear-gradient(135deg,#cfd6dc,#6f7b86 55%,#3c4550)}
.photo.family{background:linear-gradient(135deg,#e6e1d6,#b9a894 55%,#7e7466)}
.nav-arrow{position:absolute;top:224px;width:16px;height:24px}
.newsletter{position:absolute;left:334px;top:400px;width:448px;height:126px;background:var(--white);
  border:6px solid var(--blue);border-radius:4px}
.newsletter h4{position:absolute;left:44px;top:14px;font-size:14px;color:var(--title);font-weight:700}
.newsletter .env{position:absolute;left:16px;top:14px;width:20px;height:15px}
.newsletter .field{position:absolute;left:44px;top:50px;width:214px;height:26px;border:1px solid #cfd4d9;border-radius:13px;
  font-size:10px;color:#a9adb2;padding-left:14px;line-height:24px;font-style:italic}
.newsletter .subscribe{position:absolute;left:268px;top:50px;width:98px;height:26px;border-radius:13px;background:var(--navy);
  color:var(--white);font-size:12px;font-weight:700;text-align:center;line-height:26px}
.quote{position:absolute;left:812px;top:400px;width:224px;height:126px;background:var(--green);border:4px solid var(--white);
  border-radius:4px;color:var(--white);text-align:center;white-space:nowrap}
.quote .small{margin-top:26px;font-size:18px;font-weight:700}
.quote .big{font-size:27px;font-weight:700;line-height:34px}
</style>
</head>
<body>
<div class="backdrop" role="img" aria-label="Blue background with soft green swirl decoration"></div>

<aside class="social-rail">
  <span class="dot" style="top:372px"></span>
  <span class="dot" style="top:398px"></span>
  <span class="dot" style="top:424px"></span>
  <span class="dot" style="top:450px"></span>
  <span class="label">Stay Connect With Us</span>
</aside>

<nav class="sidebar">
  <div class="brand"><span class="mark"></span><span class="name">Qorvinex</span></div>
  <ul class="menu">
    <li class="active" style="top:0">Packages</li>
    <li style="top:36px">Services</li>
    <li style="top:72px">Next Step</li>
    <li style="top:108px">Career</li>
    <li style="top:144px">About</li>
  </ul>
  <p class="footer-note">Copyright © 2012 <b>Qorvinex.com</b><br>info@qorvinex.com<br>Halvard Brunsey - Ravnsvej 12 - 4180<br>Solmarke - Denmark</p>
</nav>

<svg class="nav-arrow" style="left:302px" viewBox="0 0 16 24"><path d="M13 2 3 12l10 10" fill="none" stroke="#fff" stroke-width="3"/></svg>
<svg class="nav-arrow" style="left:1036px" viewBox="0 0 16 24"><path d="M3 2l10 10L3 22" fill="none" stroke="#fff" stroke-width="3"/></svg>

<article class="teaser first" style="left:334px">
  <div class="photo laptop" role="img" aria-label="Photo of a man relaxing with a laptop"></div>
  <h3>Veltrix projects are big and costly, right? - Well, they don't have to be.</h3>
  <p>Let's talk about how we can ensure that your Veltrix project costs are kept at a minimum.</p>
  <span class="details">details</span>
</article>

<article class="teaser" style="left:566px">
  <div class="photo team" role="img" aria-label="Photo of a business team in suits"></div>
  <h3>Looking for a system to control your marketing</h3>
  <p>Then Veltrix's combined setup of software to a reduced price, and delivery, called Swift Launch Service</p>
  <span class="details">details</span>
</article>

<article class="teaser" style="left:804px">
  <div class="photo family" role="img" aria-label="Photo of a family gathered around a laptop"></div>
  <h3>Need something special for your Veltrix implementation?</h3>
  <p>Check our packages and contact us for a quote. Remember we have teamed up with an official partner.</p>
  <span class="details">details</span>
</article>

<section class="newsletter">
  <svg class="env" viewBox="0 0 20 15"><rect x="1" y="1" width="18" height="13" fill="none" stroke="#1f7cc4" stroke-width="1.5"/><path d="M1 1l9 7 9-7" fill="none" stroke="#1f7cc4" stroke-width="1.5"/></svg>
  <h4>Subscribe to Our Newsletter</h4>
  <div class="field">Type your email address</div>
  <div class="subscribe">SUBSCRIBE</div>
</section>

<section class="quote">
  <div class="small">Click Here to</div>
  <div class="big">Get a FREE Quote</div>
</section>
</body>
</html>
```